Innovative Healthcare Technology Company needs a Business Card Design

We are in need of an innovative business card design for a new healthcare software company called "Brightwell Harbor Systems". We develop software that creates medical assessment applications and mobile e-learning prevention services to reduce risk behaviors in adolescent and young adults. Our initial product, the "MERIDIAN App", conducts a tailored sexual risk assessment and provides a doctor with an insightful patient report to improve sexual risk counseling and ultimately reduce unintended pregnancy, STDs, etc.

We would like the design to incorporate our logo and branding colors (attached) in an innovative and creative manner. The final design should communicate professionalism and healthcare innovation. Our tag line is "prevention is the solution" (doesn't necessarily need to be included) and our target audience is doctors, medical directors, and medical business administrators. Please visit our website for additional info ourlantrixhub.com. Be creative and we look forward to seeing your designs!

Target Market(s)

healthcare - doctors, medical directors and medical business administrators

Industry/Entity Type

Healthcare

Contact Information for Business Card

We would like the design to incorporate our logo and branding colors (attached) in an innovative and creative manner. The final design should communicate professionalism and healthcare innovation. Our tag line is "prevention is the solution" (doesn't necessarily need to be included)

Font styles to use
Other font styles liked:
• quicksand

Requirements
Must have
• our logo and brand colors
• Name, (Joan Ferraventi, PhD)
• Email (drjoan@ourlantrixhub.com)
• phone (555.213.8870)
• Website (ourlantrixhub.com)
Should not have
• cartoon look

```html
<!DOCTYPE html>
<html lang="en">
<head>
<meta charset="utf-8">
<title>Brightwell Harbor Systems — Business Card</title>
<link rel="stylesheet" href="https://fonts.googleapis.com/css2?family=Quicksand:wght@500;600&family=Roboto:wght@400;700&display=swap">
<style>
  :root {
    --brand-blue: #0b5aa2;
    --brand-green: #6da48e;
    --ink-grey: #5a5d62;
    --card-white: #ffffff;
    --panel-tint: #eef2f5;
    --panel-tint-blue: #e6edf4;
    --stage: #e4e6e9;
  }
  * { box-sizing: border-box; margin: 0; padding: 0; }
  html, body { width: 1200px; height: 750px; overflow: hidden; }
  body {
    background: var(--stage);
    display: flex;
    align-items: center;
    justify-content: center;
    gap: 40px;
  }
  .card {
    width: 540px;
    height: 309px;
    position: relative;
    overflow: hidden;
    box-shadow: 0 6px 18px rgba(0,0,0,0.15);
  }
  .card-front {
    background: var(--brand-blue);
    display: flex;
    align-items: center;
    justify-content: center;
    gap: 14px;
  }
  .brand-mark {
    width: 22px;
    height: 22px;
    background: var(--card-white);
  }
  .brand-name {
    font-family: "Quicksand", sans-serif;
    font-weight: 500;
    font-size: 30px;
    color: var(--card-white);
    letter-spacing: 0.5px;
  }
  .card-back { background: var(--card-white); }
  .tint-panel {
    position: absolute;
    border-radius: 10px;
    background: var(--panel-tint);
  }
  .tint-panel.top { right: -20px; top: -20px; width: 190px; height: 90px; opacity: 0.7; }
  .tint-panel.middle { right: -20px; top: 92px; width: 260px; height: 92px; }
  .tint-panel.bottom { right: -20px; top: 200px; width: 300px; height: 130px; background: var(--panel-tint-blue); }
  .back-content {
    position: relative;
    padding: 70px 0 0 48px;
  }
  .back-brand {
    display: flex;
    align-items: center;
    gap: 12px;
  }
  .back-brand .brand-mark { background: var(--brand-blue); }
  .back-brand .brand-name { color: var(--brand-blue); font-size: 28px; }
  .person {
    margin: 22px 0 0 86px;
    font-family: "Roboto", sans-serif;
  }
  .person-name {
    font-weight: 700;
    font-size: 19px;
    color: var(--brand-blue);
    letter-spacing: -0.3px;
  }
  .person-name .credential { font-size: 13px; }
  .person-role {
    font-family: "Quicksand", sans-serif;
    font-weight: 500;
    font-size: 14px;
    color: var(--brand-green);
    margin-top: 1px;
  }
  .contact-list {
    list-style: none;
    margin: 16px 0 0 106px;
    font-family: "Roboto", sans-serif;
    font-size: 12.5px;
    color: var(--ink-grey);
  }
  .contact-list li {
    display: flex;
    align-items: center;
    gap: 7px;
    margin-bottom: 4px;
  }
  .contact-icon { width: 13px; height: 13px; flex: none; fill: var(--brand-blue); }
</style>
</head>
<body>
  <section class="card card-front" aria-label="Card front">
    <span class="brand-mark"></span>
    <span class="brand-name">Brightwell Harbor Systems</span>
  </section>

  <section class="card card-back" aria-label="Card back">
    <div class="tint-panel top"></div>
    <div class="tint-panel middle"></div>
    <div class="tint-panel bottom"></div>
    <div class="back-content">
      <div class="back-brand">
        <span class="brand-mark"></span>
        <span class="brand-name">Brightwell Harbor Systems</span>
      </div>
      <div class="person">
        <p class="person-name">Joan Ferraventi, <span class="credential">PhD</span></p>
        <p class="person-role">President</p>
      </div>
      <ul class="contact-list">
        <li>
          <svg class="contact-icon" viewBox="0 0 16 16" aria-hidden="true"><path d="M3.6 1.2l2.3 2.6-1.3 1.6c.9 2 2.4 3.5 4.4 4.4l1.6-1.3 2.6 2.3-1.5 2.4C7 12.9 3.1 9 1.1 2.7z"/></svg>
          <span>555.213.8870</span>
        </li>
        <li>
          <svg class="contact-icon" viewBox="0 0 16 16" aria-hidden="true"><path d="M1 3h14v10H1z M2 4v.4l6 4.2 6-4.2V4z" fill-rule="evenodd"/></svg>
          <span>drjoan@ourlantrixhub.com</span>
        </li>
        <li>
          <svg class="contact-icon" viewBox="0 0 16 16" aria-hidden="true"><circle cx="8" cy="8" r="7"/><path d="M1 8h14M8 1c2.5 2.5 2.5 11.5 0 14M8 1c-2.5 2.5-2.5 11.5 0 14" stroke="#fff" stroke-width="1" fill="none"/></svg>
          <span>ourlantrixhub.com</span>
        </li>
      </ul>
    </div>
  </section>
</body>
</html>
```